International Trading Company, 'ZOLVIQ' needs a Business Card

The company name is "ZOLVIQ" and it has own logo design.
I'd like to use its logo on this business card.
I need two side Business Card.
I'll look forward to your great design.
Thank you very much in advance.

Contact Information for Business Card

Company Name : Zolviq Harbour Limited
Information Example
Dorian Pallister
Mobile(use icon please) : 1 (212) 555-0143
Tel(use icon please) : 1 (212) 555-0178
Email(use icon please) : dorian27@zolviqharbour-mail.com
Address(use icon please) : 482 Halden Ave, New York, NY 10160, USA

```html
<!DOCTYPE html>
<html lang="en">
<head>
<meta charset="utf-8">
<title>ZOLVIQ Business Card</title>
<link rel="stylesheet" href="https://fonts.googleapis.com/css2?family=Exo+2:wght@700&family=Open+Sans:wght@400;600&display=swap">
<style>
  :root {
    --page: #e9e7e3;
    --ink-black: #141414;
    --card-white: #ffffff;
    --logo-grey: #5a5a5a;
    --text-dark: #3a3a3a;
    --text-mid: #555555;
    --rule: #6a6a6a;
    --edge-grey: #8a8a8a;
  }
  * { margin: 0; padding: 0; box-sizing: border-box; }
  html, body { width: 1200px; height: 900px; overflow: hidden; background: var(--page); }
  .canvas { position: relative; width: 1200px; height: 900px; }

  .card { position: absolute; left: 320px; width: 560px; height: 320px; box-shadow: 0 6px 18px rgba(0,0,0,.18); overflow: hidden; }

  /* Front */
  .card-front { top: 90px; background: var(--ink-black); display: flex; align-items: center; justify-content: center; }
  .front-wordmark { font-family: "Exo 2", sans-serif; font-weight: 700; font-size: 88px; letter-spacing: 3px; color: var(--card-white); }

  /* Back */
  .card-back { top: 470px; background: var(--card-white); }
  .edge { position: absolute; top: 0; bottom: 0; width: 12px; background: var(--ink-black); }
  .edge-left { left: 0; }
  .edge-right { right: 0; }
  .edge-accent { position: absolute; width: 12px; background: var(--edge-grey); }
  .edge-left .edge-accent { top: 200px; height: 36px; }
  .edge-right .edge-accent { top: 20px; height: 40px; }

  .back-wordmark { position: absolute; top: 36px; right: 48px; font-family: "Exo 2", sans-serif; font-weight: 700; font-size: 54px; line-height: 1; letter-spacing: 2px; color: var(--logo-grey); }
  .rule { position: absolute; height: 1.5px; background: var(--rule); }
  .rule-top { top: 118px; left: 40px; right: 40px; }
  .rule-contact { top: 226px; left: 44px; width: 236px; }

  .address { position: absolute; top: 140px; right: 48px; text-align: right; font-family: "Open Sans", sans-serif; font-style: normal; font-size: 13px; line-height: 1.5; color: var(--text-mid); }

  .person { position: absolute; top: 170px; left: 44px; }
  .person-name { font-family: "Exo 2", sans-serif; font-weight: 700; font-size: 18px; letter-spacing: .5px; text-transform: uppercase; color: var(--text-dark); }
  .person-title { font-family: "Open Sans", sans-serif; font-size: 14px; color: var(--text-mid); }

  .contacts { position: absolute; top: 240px; left: 44px; list-style: none; font-family: "Open Sans", sans-serif; font-size: 13px; color: var(--text-mid); }
  .contacts li { display: flex; align-items: center; gap: 12px; height: 22px; }
  .contacts svg { width: 12px; height: 12px; fill: var(--text-dark); flex: none; }
</style>
</head>
<body>
<div class="canvas">
  <section class="card card-front">
    <div class="front-wordmark">ZOLVIQ</div>
  </section>

  <section class="card card-back">
    <div class="edge edge-left"><div class="edge-accent"></div></div>
    <div class="edge edge-right"><div class="edge-accent"></div></div>

    <div class="back-wordmark">ZOLVIQ</div>
    <div class="rule rule-top"></div>

    <address class="address">482 Halden Ave, New<br>York, NY 10160, USA</address>

    <div class="person">
      <div class="person-name">Dorian Pallister</div>
      <div class="person-title">Founder</div>
    </div>
    <div class="rule rule-contact"></div>

    <ul class="contacts">
      <li><svg viewBox="0 0 12 12"><path d="M3 0h6a1 1 0 0 1 1 1v10a1 1 0 0 1-1 1H3a1 1 0 0 1-1-1V1a1 1 0 0 1 1-1zm0 1.5v8h6v-8z"/></svg>1 (212) 555-0143</li>
      <li><svg viewBox="0 0 12 12"><path d="M2.4 0.5l2 2.3-1 1.2c.7 1.6 2 2.9 3.6 3.6l1.2-1 2.3 2-1 2.3C5 10.6 1.4 7 0.1 1.5z"/></svg>1 (212) 555-0178</li>
      <li><svg viewBox="0 0 12 12"><path d="M0 2h12v1.2L6 7 0 3.2zm0 2.6l6 3.8 6-3.8V10H0z"/></svg>dorian27@zolviqharbour-mail.com</li>
    </ul>
  </section>
</div>
</body>
</html>
```